NOTE: I PROVIDED THE INCORRECT LOGO AND ONLY A HANDFUL OF PEOPLE NOTICED THAT IT WAS NOT THE ONE I DESCRIBED. THE LOGO I HAVE NOW ATTACHED MATCHES MY WEBSITE AND THE COLORS ON THE WEBSITE SHOULD BE USED FOR THE CARD.

PLEASE READ THE BUSINESS CARD DETAILS AND PROJECT MUST HAVES CAREFULLY.

I am looking for a business card that is powerful, a bit edgy, and although I work in the corporate world, not too formal. I would like to see designs that use the colors on my website www.brightmoorlane.com. I don't want the card to look washed out so please use shades of those colors that make them "pop". The "vibe" of the card needs to show substance and confidence while also reflecting that we're not your usual consultants.

The focus of my work is turning "people problems" into profits. Those problems could be poor service, an unstable workforce, untrained leaders, or managing change. We are an aggressive, results-focused team of performance improvement professionals who refuse to believe "things can't be done". For us, failure is not an option. Our logo reflects a target from the view of the site on a gun.

In addition to the contact information provided on the sample business card (do not include "turning people problems into profits"), I would like to include this statement (probably on the back):
I equip results-oriented business leaders to turn their people problems into profits in six months or less.

PLEASE NOTE THAT MY WEBSITE IS UNDER REVISION TO TONE DOWN THE MILITARY THEME, ALTHOUGH THE WARRIOR ENERGY AND FOCUS ON RESULTS REMAINS.

Target Market(s)

My clients are Mid and senior-level managers. I don't target any particular industry.

Industry/Entity Type

Consulting

Contact Information for Business Card

In addition to the contact information provided on the sample business card (DO NOT INCLUDE "turning people problems into profits"), I would like to include this statement (probably on the back):

I don't care whether the card is landscape or portrait view.

Font styles to use
Sans Serif

Requirements
Must have
• 1. be easy to read, no 6-8 point fonts!
• 2. a "vibe" that captures the eye without being too chaotic or busy
• 3. bold color, not washed out or boring - a good blend with the colors currently on my website (black, red, white, army green) but you don't need to use all of them.
• 4. all the contact information I have provided
• 5. a good blend with the colors currently on my website
• 6. Must have this quote on the back of the card: I equip results-oriented business leaders to turn their people problems into profits in six months or less.
Nice to have
• In looking at the sample images I provided for ideas, you can see that I like the way a card carries over from one side to the next.
• It would be great to find some aspect/quality/feature that I haven't seen before
Should not have
• 1. NO use of ALL CAPS
• 2. fonts that I would have to seek out and purchase (you should provide files for font if using something not standard)

```html
<!DOCTYPE html>
<html lang="en">
<head>
<meta charset="utf-8">
<title>Brightmoor Lane — Business Card</title>
<link href="https://fonts.googleapis.com/css2?family=Questrial&display=swap" rel="stylesheet">
<style>
  :root {
    --backdrop: #e4e4e4;
    --lime: #9fcc3b;
    --green-light: #a2cd3a;
    --green-mid: #79a54b;
    --green-deep: #437855;
    --ink: #060708;
    --paper: #ffffff;
    --soft-text: #c9ccce;
    --rule: #3e7f9a;
  }
  * { box-sizing: border-box; margin: 0; padding: 0; }
  html, body {
    width: 1200px; height: 1200px; overflow: hidden;
    background: linear-gradient(180deg, #f3f3f3 0%, var(--backdrop) 100%);
    font-family: "Questrial", "Century Gothic", sans-serif;
  }
  .canvas {
    width: 1200px; height: 1200px;
    display: flex; flex-direction: column; align-items: center; justify-content: center;
    gap: 60px;
  }
  .card {
    position: relative;
    width: 900px; height: 514px;
    box-shadow: 0 14px 30px rgba(0,0,0,0.22);
  }
  .card-front {
    background: linear-gradient(100deg, var(--green-light) 0%, var(--green-mid) 50%, var(--green-deep) 100%);
    display: flex; flex-direction: column; align-items: center; justify-content: center;
    gap: 34px;
  }
  .wordmark {
    display: flex; align-items: center; gap: 16px;
    font-size: 64px; line-height: 1; letter-spacing: 0.5px;
  }
  .wordmark-mark { width: 26px; height: 26px; flex: none; }
  .card-front .wordmark { color: var(--paper); }
  .card-front .wordmark-mark { background: var(--paper); }

  .statement {
    max-width: 600px;
    text-align: center;
    color: var(--paper);
    font-size: 22px; line-height: 1.45;
  }

  .card-back { background: var(--ink); color: var(--soft-text); }
  .card-back .wordmark {
    position: absolute; left: 90px; top: 150px;
    font-size: 42px; color: var(--lime);
  }
  .card-back .wordmark-mark { width: 18px; height: 18px; background: var(--lime); }

  .address {
    position: absolute; left: 110px; top: 360px;
    font-size: 19px; line-height: 1.35; font-style: normal;
  }
  .address-company { color: var(--lime); }

  .contact {
    position: absolute; left: 540px; top: 150px; width: 320px;
  }
  .contact-name { color: var(--lime); font-size: 30px; line-height: 1.2; }
  .contact-title { font-size: 19px; margin-top: 4px; }
  .contact-rule { height: 1px; background: var(--rule); margin: 16px 0 14px; }
  .contact-list { list-style: none; font-size: 19px; line-height: 1.55; }
  .contact-list li { display: flex; align-items: center; gap: 10px; }
  .contact-list svg { width: 16px; height: 16px; flex: none; fill: var(--lime); }
</style>
</head>
<body>
<main class="canvas">
  <section class="card card-front" aria-label="Card front">
    <div class="wordmark"><span class="wordmark-mark"></span><span>Brightmoor Lane</span></div>
    <p class="statement">I equip results-oriented business leaders to turn their people problems into profits in six months or less.</p>
  </section>

  <section class="card card-back" aria-label="Card back">
    <div class="wordmark"><span class="wordmark-mark"></span><span>Brightmoor Lane</span></div>

    <address class="address">
      <div class="address-company">Brightmoor Lane, Inc.</div>
      <div>2210 Orchard Ridge Road</div>
      <div>#410, Lakeview, MI 49000</div>
    </address>

    <div class="contact">
      <div class="contact-name">Dana Whitfield</div>
      <div class="contact-title">Chief Performance Strategist</div>
      <div class="contact-rule"></div>
      <ul class="contact-list">
        <li>
          <svg viewBox="0 0 16 16" aria-hidden="true"><path d="M8 1a7 7 0 1 0 0 14A7 7 0 0 0 8 1zm0 1.5c.8 0 1.7 1.6 2 4H6c.3-2.4 1.2-4 2-4zM5.9 2.9C5.3 3.9 4.9 5.1 4.7 6.5H2.6a5.5 5.5 0 0 1 3.3-3.6zm4.2 0a5.5 5.5 0 0 1 3.3 3.6h-2.1c-.2-1.4-.6-2.6-1.200-3.6zM2.6 8h2.1c.1 1.4.5 2.6 1.2 3.6A5.5 5.5 0 0 1 2.6 8zm3.4 0h4c-.3 2.4-1.2 4-2 4s-1.7-1.6-2-4zm5.3 0h2.1a5.5 5.5 0 0 1-3.3 3.6c.6-1 1-2.2 1.2-3.6z"/></svg>
          www.brightmoorlane.com
        </li>
        <li>
          <svg viewBox="0 0 16 16" aria-hidden="true"><path d="M1 3h14v10H1zM2.5 4.5 8 9l5.5-4.5z"/></svg>
          dana@brightmoorlane.com
        </li>
        <li>
          <svg viewBox="0 0 16 16" aria-hidden="true"><path d="M4 1.5 6.2 4 5 5.6c.8 1.8 2.6 3.6 4.4 4.4L11 8.8l2.5 2.2-1.3 2.5C7 13.2 2.8 9 2.5 3z"/></svg>
          555 - 014 - 2230
        </li>
        <li>
          <svg viewBox="0 0 16 16" aria-hidden="true"><path d="M4.5 1h7v14h-7zM6 2.5v9h4v-9zM7.3 12.5h1.4v1.2H7.3z"/></svg>
          555 - 017 - 4481
        </li>
      </ul>
    </div>
  </section>
</main>
</body>
</html>
```